Business card design needed

I need a business card for my Sydney Painting Business, that specialises in painting High -end residential homes. i want the design to look clean, modern and edgy. i also want a logo next to the RL Decorating, using RLD together.

Industry/Entity Type

Residential

Contact Information for Business Card

RL Decorating (business name),LIC 871536K, Rob Lindqvist, robert.lindqvist@brushmail.example, mobile 0419352807

```html
<!DOCTYPE html>
<html lang="en">
<head>
<meta charset="utf-8">
<title>RL Decorating – Business Card</title>
<link rel="stylesheet" href="https://fonts.googleapis.com/css2?family=Kalam:wght@400;700&family=Caveat:wght@500&display=swap">
<style>
  :root {
    --backdrop: #e7e4dc;
    --card: #cfcfcc;
    --card-shade: rgba(0, 0, 0, 0.28);
    --olive: #6a6b2c;
    --olive-bright: #a6a22a;
    --olive-dark: #3f4019;
    --ink: #2e2f25;
    --tint: #dedbc4;
  }
  * { box-sizing: border-box; margin: 0; padding: 0; }
  html, body {
    width: 1200px;
    height: 675px;
    overflow: hidden;
    background: var(--backdrop);
  }
  .sheet {
    position: relative;
    width: 1200px;
    height: 675px;
    display: flex;
    align-items: center;
    justify-content: center;
    gap: 60px;
  }
  .card {
    position: relative;
    width: 525px;
    height: 300px;
    background: var(--card);
    box-shadow: 0 6px 18px var(--card-shade);
    overflow: hidden;
  }

  /* Front */
  .card--front {
    display: flex;
    align-items: center;
    justify-content: center;
  }
  .brand {
    display: flex;
    align-items: center;
    gap: 12px;
  }
  .brand__mark {
    width: 26px;
    height: 26px;
    background: var(--olive-bright);
  }
  .brand__name {
    font-family: "Kalam", cursive;
    font-weight: 700;
    font-size: 34px;
    color: var(--olive);
    line-height: 1;
  }

  /* Back */
  .card--back { padding: 26px 30px; }
  .card--back::after {
    content: "";
    position: absolute;
    left: 0; right: 0; bottom: 0;
    height: 10px;
    background: var(--olive);
  }
  .back-brand {
    position: absolute;
    top: 22px;
    right: 28px;
    text-align: right;
  }
  .back-brand__name {
    font-family: "Kalam", cursive;
    font-weight: 700;
    font-size: 26px;
    color: var(--ink);
    line-height: 1.1;
  }
  .back-brand__licence {
    font-family: "Kalam", cursive;
    font-size: 15px;
    letter-spacing: 1px;
    color: var(--ink);
  }
  .back-decor {
    position: absolute;
    right: 40px;
    top: 92px;
    width: 120px;
    height: 120px;
    background: var(--tint);
    opacity: 0.7;
  }
  .contact {
    position: absolute;
    left: 30px;
    bottom: 34px;
  }
  .contact__name {
    font-family: "Caveat", cursive;
    font-weight: 500;
    font-size: 36px;
    color: var(--olive-dark);
    margin-bottom: 10px;
  }
  .contact__row {
    display: flex;
    align-items: center;
    gap: 14px;
    margin-top: 8px;
    font-family: "Kalam", cursive;
    font-size: 19px;
    color: var(--ink);
  }
  .contact__icon {
    width: 26px;
    height: 24px;
    border-radius: 4px;
    background: var(--olive);
    display: flex;
    align-items: center;
    justify-content: center;
  }
  .contact__icon svg { width: 16px; height: 16px; }
</style>
</head>
<body>
  <main class="sheet">
    <section class="card card--front" aria-label="Card front">
      <div class="brand">
        <span class="brand__mark"></span>
        <span class="brand__name">RL Decorating</span>
      </div>
    </section>

    <section class="card card--back" aria-label="Card back">
      <div class="back-brand">
        <div class="back-brand__name">RL Decorating</div>
        <div class="back-brand__licence">LIC 871536K</div>
      </div>
      <div class="back-decor"></div>

      <div class="contact">
        <div class="contact__name">Rob Lindqvist</div>
        <div class="contact__row">
          <span class="contact__icon">
            <svg viewBox="0 0 24 24" aria-hidden="true">
              <path fill="#e6e4d2" d="M6.6 10.8a15.1 15.1 0 0 0 6.6 6.6l2.2-2.2c.3-.3.7-.4 1-.2 1.1.4 2.3.6 3.6.6.6 0 1 .4 1 1V20c0 .6-.4 1-1 1A17 17 0 0 1 3 4c0-.6.4-1 1-1h3.5c.6 0 1 .4 1 1 0 1.3.2 2.5.6 3.6.1.3 0 .7-.2 1z"/>
            </svg>
          </span>
          <span class="contact__text">0419352807</span>
        </div>
        <div class="contact__row">
          <span class="contact__icon">
            <svg viewBox="0 0 24 24" aria-hidden="true">
              <rect x="3" y="6" width="18" height="12" fill="none" stroke="#e6e4d2" stroke-width="2"/>
              <path d="M3 6l9 7 9-7" fill="none" stroke="#e6e4d2" stroke-width="2"/>
            </svg>
          </span>
          <span class="contact__text">robert.lindqvist@brushmail.example</span>
        </div>
      </div>
    </section>
  </main>
</body>
</html>
```